We do the same thing as http://harborledger.com. We are called tidemarkfunds.com. Need a fast loading website which targets the same demographics as harborledger.com. That means a website that is full of energy and excitement, capture concepts of volcano, explosiveness and profit.

Use all content from their site as placeholder.

```html
<!DOCTYPE html>
<html lang="en">
<head>
<meta charset="utf-8">
<title>Tidemark Picks – Free Penny Stock Alerts</title>
<link href="https://fonts.googleapis.com/css2?family=Oswald:wght@500;600;700&family=Roboto+Condensed:wght@700&display=swap" rel="stylesheet">
<style>
:root{
  --black:#000;
  --panel:#2c2c2c;
  --panel-edge:#c9a227;
  --gold:#f2b31b;
  --white:#fff;
  --red:#e8251b;
  --orange:#f04a14;
  --orange-dark:#b8260a;
  --blue:#2fa6d6;
  --blue-dark:#1c6f96;
  --text:#e6e6e6;
}
*{box-sizing:border-box;margin:0;padding:0}
html,body{width:893px;height:1200px;overflow:hidden;background:var(--black)}
body{position:relative;font-family:Arial,Helvetica,sans-serif;color:var(--text)}
.abs{position:absolute}
.glitter{left:0;top:0;width:893px;height:260px;background:radial-gradient(ellipse at 20% 40%,#b3130c 0%,#5a0804 45%,#000 90%),#000}
.glitter::after{content:"";position:absolute;inset:0;background:radial-gradient(ellipse at 85% 35%,rgba(200,30,15,.8),rgba(0,0,0,0) 55%)}
.flames{left:0;top:1040px;width:893px;height:160px;background:linear-gradient(to bottom,rgba(0,0,0,0) 0%,#7a1405 30%,#e2400c 65%,#f9a21c 100%)}
.panel{left:141px;top:180px;width:575px;height:873px;background:var(--panel);border:1px solid var(--panel-edge);border-top:none}
.chart{left:300px;top:48px;width:416px;height:132px;background:linear-gradient(135deg,#020a2a,#0c2f7a 60%,#06123a)}
.ribbon{left:315px;top:14px;width:426px;height:48px;background:var(--white);transform:rotate(-4deg);border-radius:4px;box-shadow:0 3px 6px rgba(0,0,0,.5);display:flex;align-items:center;justify-content:center;font-family:'Oswald',sans-serif;font-weight:500;font-size:17px;color:#111;letter-spacing:.3px}
.ribbon b{font-weight:700;font-size:20px;margin:0 4px}
.ribbon em{font-style:italic;font-weight:700;color:var(--red);font-size:21px;margin-left:5px}
.brand{left:122px;top:86px;width:200px;font-family:'Oswald',sans-serif;font-weight:700;font-size:40px;line-height:46px;color:var(--gold);text-align:center;letter-spacing:2px}
.heading{left:141px;width:575px;text-align:center;font-family:'Oswald',sans-serif;font-weight:600;color:var(--gold);text-transform:uppercase}
.heading span{color:var(--white)}
.h-main{top:218px;font-size:31px}
.h-news{top:706px;font-size:24px}
.perks{left:162px;width:540px;display:flex;font-family:'Roboto Condensed',sans-serif;font-weight:700;font-size:12px;line-height:19px;color:var(--white)}
.perk{display:flex;gap:6px}
.perk:nth-child(1){width:179px}.perk:nth-child(2){width:198px}
.perk svg{flex:none;margin-top:2px}
.perk .hot{color:var(--red);font-style:italic}
.band{left:129px;width:587px;height:74px;background:linear-gradient(to bottom,#ff7a2a,var(--orange) 50%,var(--orange-dark));box-shadow:0 4px 8px rgba(0,0,0,.6);display:flex;align-items:center;padding-left:35px}
.email{width:401px;height:32px;border-radius:5px;background:var(--white);border:2px solid #d9d9d9;font-family:'Roboto Condensed',sans-serif;font-size:15px;color:#666;padding:6px 10px}
.signup{margin-left:8px;width:112px;height:32px;border-radius:4px;background:linear-gradient(var(--blue),var(--blue-dark));font-family:'Oswald',sans-serif;font-weight:600;font-size:22px;color:#0c3954;text-align:center;line-height:32px}
.pick{top:479px;width:118px;height:118px;border-radius:50%;background:radial-gradient(circle,#000 54%,#ff8c1a 58%,#c9300a 70%,rgba(60,20,5,.2) 100%)}
.pick-label{position:absolute;inset:0;display:flex;flex-direction:column;align-items:center;justify-content:center}
.ticker{font-family:'Oswald',sans-serif;font-weight:600;font-size:27px;line-height:30px;color:var(--gold)}
.gain{font-family:'Roboto Condensed',sans-serif;font-weight:700;font-size:12px;color:var(--white)}
.col{top:850px;width:166px}
.col h3{font-family:'Roboto Condensed',sans-serif;font-weight:700;font-size:15px;line-height:18px;color:var(--gold);margin-bottom:10px}
.col p{font-size:9px;line-height:11.5px;text-align:justify;margin-bottom:11px}
.footer{left:0;top:1058px;width:893px;text-align:center;font-size:8.5px;line-height:13px;color:var(--white)}
.footer a{color:var(--red);text-decoration:none}
</style>
</head>
<body>
<div class="abs glitter" role="img" aria-label="Sparkling red glitter background"></div>
<div class="abs flames" role="img" aria-label="Rising flames along the bottom edge"></div>

<main class="abs panel"></main>

<div class="abs chart" role="img" aria-label="Glowing blue stock chart">
  <svg width="416" height="132" viewBox="0 0 416 132"><polyline fill="none" stroke="#6fb6ff" stroke-width="2" points="10,110 50,95 80,100 110,78 140,86 170,60 200,70 235,48 260,58 290,36 320,44 350,24 390,30 410,18"/></svg>
</div>
<div class="abs ribbon">RECEIVE <b>HOT</b> PENNY STOCK <b>ALERTS</b> FOR <em>FREE!</em></div>
<div class="abs brand">TIDEMARK<br>PICKS</div>

<h1 class="abs heading h-main">Sign up for <span>free</span> penny stock alerts!</h1>

<div class="abs perks" style="top:271px">
  <div class="perk"><svg width="16" height="14" viewBox="0 0 16 14"><path d="M1 7l5 5L15 1" fill="none" stroke="#f2b31b" stroke-width="3"/></svg><span>Join the Most Explosive Penny Stock Newsletter on the WEB ... <span class="hot">100% FREE</span></span></div>
  <div class="perk"><svg width="16" height="14" viewBox="0 0 16 14"><path d="M1 7l5 5L15 1" fill="none" stroke="#f2b31b" stroke-width="3"/></svg><span>HOT Penny <span class="hot">Stock Alerts</span> Delivered Directly to your Email</span></div>
  <div class="perk"><svg width="16" height="14" viewBox="0 0 16 14"><path d="M1 7l5 5L15 1" fill="none" stroke="#f2b31b" stroke-width="3"/></svg><span><span class="hot">Don't hesitate!</span> There are LIMITED spots available.</span></div>
</div>

<form class="abs band" style="top:363px"><div class="email">Enter your email address...</div><div class="signup">SIGN UP</div></form>

<div class="abs pick" style="left:174px" role="img" aria-label="Fiery ring"><div class="pick-label"><span class="ticker">RVTQ</span><span class="gain">840% GAIN</span></div></div>
<div class="abs pick" style="left:306px" role="img" aria-label="Fiery ring"><div class="pick-label"><span class="ticker">MKLD</span><span class="gain">800% GAIN</span></div></div>
<div class="abs pick" style="left:437px" role="img" aria-label="Fiery ring"><div class="pick-label"><span class="ticker">TPRW</span><span class="gain">212% GAIN</span></div></div>
<div class="abs pick" style="left:567px" role="img" aria-label="Fiery ring"><div class="pick-label"><span class="ticker">GLVN</span><span class="gain">142% GAIN</span></div></div>

<div class="abs perks" style="top:623px">
  <div class="perk"><svg width="16" height="14" viewBox="0 0 16 14"><path d="M1 7l5 5L15 1" fill="none" stroke="#f2b31b" stroke-width="3"/></svg><span>Join the Most Explosive Penny Stock Newsletter on the WEB ... <span class="hot">100% FREE</span></span></div>
  <div class="perk"><svg width="16" height="14" viewBox="0 0 16 14"><path d="M1 7l5 5L15 1" fill="none" stroke="#f2b31b" stroke-width="3"/></svg><span>HOT Penny <span class="hot">Stock Alerts</span> Delivered Directly to your Email</span></div>
  <div class="perk"><svg width="16" height="14" viewBox="0 0 16 14"><path d="M1 7l5 5L15 1" fill="none" stroke="#f2b31b" stroke-width="3"/></svg><span><span class="hot">Don't hesitate!</span> There are LIMITED spots available.</span></div>
</div>

<h2 class="abs heading h-news">Sign up for <span>free tidemark picks</span> newsletter</h2>

<form class="abs band" style="top:752px"><div class="email">Enter your email address...</div><div class="signup">SIGN UP</div></form>

<section class="abs col" style="left:162px">
  <h3>FREE Daily Penny Stocks Picks</h3>
  <p>Our newsletters are completely FREE. We do not charge anything to our subscribers. Feel free to share our website with your family &amp; friends.</p>
  <p>We send newsletters on a regular basis on different stocks. You will most likely receive at least one "Pick of the Day"1 - 3 time / week. We try to take our time in choosing our stock picks to make sure our members have the best opportunity to make profits on our picks.</p>
</section>
<section class="abs col" style="left:342px">
  <h3>Tidemark Picks!!!</h3>
  <p>Tidemarkfunds.com was created to help public companies get their stories out to investors and help investors find stocks about to make potentially big moves.</p>
  <p>If you're looking for early alerts on potentially fast moving stocks, with high potential for gains, then you've found a tremendous resource. It is much easier for a stock to go from .05 to .50 than it is to go from $5 to $50. Not every pick will be profitable, but with effective stop loss techniques employed in your trading, profiting from our alerts is very achievable.</p>
</section>
<section class="abs col" style="left:522px">
  <h3>FREE Stock Alerts</h3>
  <p>Whenever there is a trading opportunity, we will send you a Stock Alert E-Mail at any time of the day which you can trade. We do all the reseach for you, all you have to do is put the trade on.</p>
  <p>Tidemark Stock Alerts provide early trade alerts whenever our team sees them. We consistently pick winning trades, sign up to start following our alerts now.</p>
</section>

<footer class="abs footer">
  100% Anti-Spam &amp; will never rent or sell your information!<br>
  Unsubscribe at any time simply by clicking a link found at the bottom of any email you receive from us.<br>
  <a href="#">Privacy Policy</a> | <a href="#">Disclaimer</a>
</footer>
</body>
</html>
```